Keen Motion Powerpoint Template

We need a Powerpoint Template design for a new company based in Ottawa (Canada), called Keen Motion. We help team sport coaches and sport programs improve their teams and develop their athletes better.

Basically, I would like to have a professionnal, beautiful, and minimalist powerpoint template that I could then used to support the workshops, courses, and keynote presentations I give.

Attached is a file that contains all the information necessary for our logos, colors, and fonts. I would have to be able to present the "template" either as Keen Motion (Corporate ID) or as Coach Dorian (personal brand).

Thank you for your interest,

Target Market(s)

Athletic Directors of Universities, High-Performance Team Sport Coaches

Industry/Entity Type

It Company

Font styles to use
Sans Serif

Requirements
Must have
• These are all template slides that I would like to have designed (I will fill them with the content for each presentation): (a) Title slide, (b) Heading and text slide, (c) 2 large images with subtitles, (d) 3 large images with subtitles, (e) large image with text, (f) large image with subtitle, (g) quote slide, and (h) 3 key points
Nice to have
• Personalized to Coach Dorian and Keen Motion, but not mandatory. The emphasis should NOT be put on the brand, but rather on the ability for viewers to see the text and understand the message.

```html
<!DOCTYPE html>
<html lang="en">
<head>
<meta charset="utf-8">
<title>Keen Motion Presentation Template</title>
<link href="https://fonts.googleapis.com/css2?family=Oswald:wght@400;600&family=Open+Sans:wght@300;400;600;700&display=swap" rel="stylesheet">
<style>
:root{
  --page:#2a2a2a;
  --paper:#ffffff;
  --ink:#1e1e1e;
  --grey:#8a8a8a;
  --soft:#e6e6e6;
  --accent:#ec5a24;
  --blue:#2f6cc9;
  --navy:#1c2248;
  --dark:#141414;
  --track-blue:linear-gradient(165deg,#2c5fb0 0%,#3d83d6 55%,#6aa2e0 100%);
  --track-red:linear-gradient(170deg,#a8473b 0%,#c85a43 60%,#d9735a 100%);
  --photo-dark:linear-gradient(150deg,#090909 0%,#2b2b2b 55%,#5a5a5a 100%);
  --photo-gym:linear-gradient(160deg,#1d1d1d 0%,#4a3a36 50%,#7a2c2c 100%);
}
*{box-sizing:border-box;margin:0;padding:0}
html,body{width:1200px;height:1200px;overflow:hidden;background:var(--page)}
body{font-family:"Open Sans",Arial,sans-serif;color:var(--ink)}
.deck{position:absolute;left:2px;top:4px;display:grid;grid-template-columns:repeat(6,196px);grid-auto-rows:110px;column-gap:4px;row-gap:10px}
.slide{position:relative;overflow:hidden;background:var(--paper)}
.slide.dark{background:var(--dark)}
.abs{position:absolute}
.title{position:absolute;left:0;right:0;top:12px;text-align:center;font-family:"Oswald",Arial,sans-serif;font-weight:600;font-size:10px;letter-spacing:.2px;text-transform:uppercase;color:var(--ink)}
.title.sans{font-family:"Open Sans",Arial,sans-serif;font-weight:700;font-size:9px}
.title.light{color:#fff}
.sub{position:absolute;left:0;right:0;top:25px;text-align:center;font-size:2.4px;color:var(--grey)}
.copy{font-size:2.6px;line-height:1.45;color:var(--grey)}
.copy.white{color:#e8e8e8}
.label{font-size:2.6px;font-weight:700;text-transform:uppercase;color:var(--ink)}
.foot{position:absolute;left:8px;bottom:5px;font-size:2.4px;font-weight:700;color:var(--ink)}
.dark .foot{color:#ddd}
.pnum{position:absolute;right:6px;top:5px;width:5px;height:5px;border:.5px solid #ccc;border-radius:50%}
.mark{position:absolute;right:7px;bottom:4px;width:5px;height:5px;background:var(--accent)}
.ph{position:absolute}
.track{background:var(--track-blue)}
.track-r{background:var(--track-red)}
.shot{background:var(--photo-dark)}
.gym{background:var(--photo-gym)}
.face{background:linear-gradient(160deg,#d9cfc6,#a99889)}
.btn{position:absolute;border:.6px solid var(--ink);font-size:2.2px;font-weight:700;text-align:center;line-height:5px;text-transform:uppercase}
.ico{position:absolute;width:9px;height:9px;border:.7px solid var(--ink);border-radius:50%}
.ico.fill{background:var(--ink);border-color:var(--ink)}
.ico.blue{background:var(--blue);border-color:var(--blue)}
.ico.orange{background:var(--accent);border-color:var(--accent)}
.big{font-family:"Oswald",Arial,sans-serif;font-weight:600;text-transform:uppercase;line-height:1}
.numrow{position:absolute;font-size:8px;font-weight:400;text-align:center;width:30px}
.bar{position:absolute;height:3px;background:var(--soft)}
.bar i{display:block;height:100%;background:var(--ink)}
.bar.g i{background:var(--grey)}
</style>
</head>
<body>
<main class="deck">

<!-- row 1 -->
<section class="slide dark">
  <div class="ph gym" style="inset:0" role="img" aria-label="Athletes training in a gym, dark photo"></div>
  <div class="abs big" style="left:30px;top:30px;width:96px;height:24px;border:1px solid #fff;color:#fff;font-size:13px;text-align:center;line-height:22px">KEEN MOTION</div>
  <div class="abs" style="left:30px;top:57px;font-size:2.4px;color:#ddd">PRESENTATION BY COACH DORIAN</div>
  <div class="abs big" style="left:54px;top:64px;width:32px;height:18px;background:#fff;color:var(--ink);font-size:5px;text-align:center;padding-top:4px">KEEN<br>MOTION</div>
</section>

<section class="slide">
  <div class="pnum"></div>
  <div class="ph face" style="left:22px;top:28px;width:36px;height:40px;clip-path:polygon(50% 0,100% 25%,100% 75%,50% 100%,0 75%,0 25%)" role="img" aria-label="Portrait of the coach"></div>
  <div class="btn" style="left:26px;top:73px;width:28px;height:5px">Coach Dorian</div>
  <div class="abs big" style="left:66px;top:36px;font-size:9px;color:var(--accent)">Welcome Message</div>
  <p class="abs copy" style="left:66px;top:50px;width:110px">Share a warm opening note with your audience here. Explain who you are, what this session covers and why it matters to the coaches in the room today.</p>
  <div class="foot">KEEN MOTION</div><div class="mark"></div>
</section>

<section class="slide">
  <div class="pnum"></div>
  <div class="title">Text in One Column</div>
  <div class="sub">Modern and Minimal Presentation Template</div>
  <p class="abs copy" style="left:16px;top:36px;width:164px">Write one full column of text here to introduce the topic. Keep sentences short so the audience can read every line from the back of the room. Add a second thought that supports the main idea and gives one clear example from the field. Finish the block with the key message you want your team to remember after the workshop ends.</p>
  <p class="abs copy" style="left:16px;top:64px;width:164px">Use a second block to add more detail. Describe the drill, the goal of the session and how coaches can measure progress with their athletes each week of the season.</p>
  <div class="foot">KEEN MOTION</div><div class="mark"></div>
</section>

<section class="slide">
  <div class="pnum"></div>
  <div class="abs big" style="left:16px;top:14px;font-size:8px;line-height:1.05">Creative<br>Text<br>Layouts</div>
  <p class="abs copy" style="left:16px;top:52px;width:70px">Start with a short lead that sets the tone for this part of the talk and names the main theme.</p>
  <p class="abs copy" style="left:100px;top:14px;width:80px">Add the main text in this right column. Explain the idea in simple words, give one example and close with a clear point.</p>
  <p class="abs copy" style="left:100px;top:40px;width:80px">Use this second block for extra detail about the method, the data or the story behind the idea you share.</p>
  <div class="foot">KEEN MOTION</div><div class="mark"></div>
</section>

<section class="slide">
  <div class="pnum"></div>
  <div class="title">Text in Three Column</div>
  <div class="sub">Modern and Minimal Presentation Template</div>
  <p class="abs copy" style="left:16px;top:36px;width:50px">Write the first point here in a few short lines that explain one clear idea to the room.</p>
  <p class="abs copy" style="left:73px;top:36px;width:50px">Write the second point here and link it to the first with one simple example.</p>
  <p class="abs copy" style="left:130px;top:36px;width:50px">Write the third point here and finish with the key message to remember.</p>
  <div class="foot">KEEN MOTION</div><div class="mark"></div>
</section>

<section class="slide">
  <div class="pnum"></div>
  <div class="title">About Us</div>
  <p class="abs copy" style="left:20px;top:26px;width:156px;text-align:center">A short line about who we are and how we help coaches build stronger teams.</p>
  <div class="btn" style="left:84px;top:34px;width:28px;height:5px">Our History</div>
  <div class="ph gym" style="left:0;right:0;top:44px;bottom:0" role="img" aria-label="Gym floor with weights and an athlete"></div>
</section>

<!-- row 2 -->
<section class="slide">
  <div class="pnum"></div>
  <div class="title">Content Overview</div>
  <div class="ico" style="left:36px;top:34px"></div><div class="ico" style="left:67px;top:34px"></div><div class="ico" style="left:98px;top:34px"></div><div class="ico" style="left:129px;top:34px"></div>
  <div class="ico" style="left:36px;top:64px"></div><div class="ico" style="left:67px;top:64px"></div><div class="ico" style="left:98px;top:64px"></div><div class="ico" style="left:129px;top:64px"></div>
  <div class="abs label" style="left:32px;top:47px">Welcome</div><div class="abs label" style="left:64px;top:47px">About Us</div><div class="abs label" style="left:93px;top:47px">Our Mission</div><div class="abs label" style="left:126px;top:47px">Our Vision</div>
  <div class="abs label" style="left:32px;top:77px">Our Team</div><div class="abs label" style="left:62px;top:77px">Our Services</div><div class="abs label" style="left:92px;top:77px">Our Portfolio</div><div class="abs label" style="left:125px;top:77px">Our Devices</div>
  <div class="foot">KEEN MOTION</div><div class="mark"></div>
</section>

<section class="slide">
  <div class="pnum"></div>
  <div class="title" style="color:var(--accent)">Timeline</div>
  <div class="sub">Modern and Minimal Presentation Template</div>
  <div class="abs" style="left:97px;top:30px;width:.6px;height:70px;background:#999"></div>
  <div class="btn" style="left:86px;top:30px;width:22px;height:5px">Our History</div>
  <div class="ph shot" style="left:40px;top:52px;width:42px;height:24px" role="img" aria-label="Athletes celebrating"></div>
  <div class="ph track" style="left:110px;top:64px;width:42px;height:24px" role="img" aria-label="Running track lanes"></div>
  <div class="foot">KEEN MOTION</div><div class="mark"></div>
</section>

<section class="slide">
  <div class="pnum"></div>
  <div class="abs" style="left:82px;top:8px;width:.6px;height:94px;background:#999"></div>
  <div class="ph shot" style="left:40px;top:14px;width:36px;height:22px" role="img" aria-label="Athlete raising arms"></div>
  <div class="ph track" style="left:88px;top:32px;width:36px;height:22px" role="img" aria-label="Running track lanes"></div>
  <div class="ph shot" style="left:40px;top:58px;width:36px;height:22px" role="img" aria-label="Team celebrating"></div>
  <p class="abs copy" style="left:88px;top:74px;width:46px">A short milestone note for this year.</p>
  <div class="foot">KEEN MOTION</div><div class="mark"></div>
</section>

<section class="slide">
  <div class="pnum"></div>
  <div class="title">About Us</div>
  <div class="sub">Modern and Minimal Presentation Template</div>
  <div class="abs" style="left:30px;top:44px;width:72px;height:42px;border:.8px solid var(--ink);background:#fff;z-index:2"></div>
  <div class="abs big" style="left:30px;top:50px;width:72px;text-align:center;font-size:6px;z-index:3">What We Do?</div>
  <p class="abs copy" style="left:36px;top:60px;width:60px;text-align:center;z-index:3">Explain in two lines what your program offers to teams.</p>
  <div class="btn" style="left:56px;top:76px;width:20px;height:5px;z-index:3">Thanks</div>
  <div class="ph shot" style="left:94px;top:38px;width:82px;height:54px" role="img" aria-label="Boxer training in dark light"></div>
  <div class="foot">KEEN MOTION</div><div class="mark"></div>
</section>

<section class="slide">
  <div class="pnum"></div>
  <div class="title">Our Mission</div>
  <div class="abs" style="left:28px;top:34px;width:52px;height:62px;border:.5px solid #ddd"></div>
  <div class="abs big" style="left:34px;top:52px;font-size:7px;line-height:1">I Want<br>To Be<br>Your<br>Friend</div>
  <div class="ico" style="left:98px;top:36px;border-radius:2px;border-color:var(--blue)"></div><div class="ico" style="left:144px;top:36px;border-radius:2px;border-color:var(--blue)"></div>
  <div class="ico" style="left:98px;top:64px;border-radius:2px;border-color:var(--blue)"></div><div class="ico" style="left:144px;top:64px;border-radius:2px;border-color:var(--accent)"></div>
  <p class="abs copy" style="left:98px;top:48px;width:36px">Clear goals for every team.</p><p class="abs copy" style="left:144px;top:48px;width:36px">Support each athlete.</p>
  <p class="abs copy" style="left:98px;top:76px;width:36px">Better daily training.</p><p class="abs copy" style="left:144px;top:76px;width:36px">Growth you can measure.</p>
  <div class="foot">KEEN MOTION</div><div class="mark"></div>
</section>

<section class="slide">
  <div class="pnum"></div>
  <div class="title">Our Business</div>
  <p class="abs copy" style="left:28px;top:26px;width:140px;text-align:center">Tell the story of your business in one clear line that coaches and directors can follow.</p>
  <div class="ph track-r" style="left:0;top:54px;width:70px;height:56px" role="img" aria-label="Track with lane numbers"></div>
  <div class="ph track" style="left:70px;top:54px;width:60px;height:56px" role="img" aria-label="Blue track lanes"></div>
  <div class="ph shot" style="left:130px;top:54px;width:66px;height:56px" role="img" aria-label="Athlete in dark arena"></div>
</section>

<!-- row 3 -->
<section class="slide">
  <div class="ph track-r" style="left:0;top:0;width:98px;height:42px" role="img" aria-label="Red running track"></div>
  <div class="ph track" style="left:98px;top:56px;width:98px;height:54px" role="img" aria-label="Blue track lanes with numbers"></div>
  <p class="abs" style="left:108px;top:10px;width:80px;font-size:3.2px;line-height:1.4;color:#444">"The price of success is hard work and the will to give your best in every single practice you attend."</p>
  <div class="abs label" style="left:108px;top:36px;font-size:3.2px">Victor Lambert</div>
  <p class="abs" style="left:8px;top:62px;width:82px;font-size:3.2px;line-height:1.4;color:#444;text-align:right">"Desire is the key to motivation, but it is the daily commitment that makes a champion."</p>
  <div class="abs label" style="left:50px;top:84px;font-size:3.2px">Marco Ardent</div>
</section>

<section class="slide" style="background:linear-gradient(120deg,#2b3f7a 0%,#b2533f 55%,#f07a24 100%)">
  <div class="ph" style="inset:0;background:linear-gradient(180deg,rgba(0,0,0,.1),rgba(0,0,0,0))" role="img" aria-label="Track lanes under warm light"></div>
  <div class="abs" style="left:28px;top:34px;width:140px;height:42px;border:.7px solid rgba(255,255,255,.8)"></div>
  <div class="abs label" style="left:28px;top:44px;width:140px;text-align:center;color:#fff;font-size:3.6px">Our Vision</div>
  <p class="abs copy white" style="left:38px;top:52px;width:120px;text-align:center">Describe where your program is going and the change you want to bring to every team you work with.</p>
</section>

<section class="slide">
  <div class="pnum"></div>
  <div class="title">My Profile</div>
  <div class="btn" style="left:36px;top:36px;width:24px;height:4px">Awards</div><div class="btn" style="left:86px;top:36px;width:24px;height:4px">Skills</div><div class="btn" style="left:136px;top:36px;width:24px;height:4px">My Jobs</div>
  <div class="abs copy" style="left:30px;top:46px;width:36px;text-align:center"><b style="color:#333">Coaching Prize 2017</b><br>Sports Award<br><br><b style="color:#333">Awards of Merit</b><br>Design Medal<br><br><b style="color:#333">Club Week Award</b><br>Local Event</div>
  <div class="abs copy" style="left:80px;top:46px;width:36px;text-align:center"><b style="color:#333">Team Vision</b><br>Advanced<br><br><b style="color:#333">Key Skill</b><br>Expert<br><br><b style="color:#333">Hope</b><br>Strong<br><br><b style="color:#333">Running</b><br>Daily</div>
  <div class="abs copy" style="left:130px;top:46px;width:36px;text-align:center"><b style="color:#333">Head Coach</b><br>2015 - 2017<br><br><b style="color:#333">Program Lead</b><br>2013 - 2015<br><br><b style="color:#333">Mentor Role</b><br>2011 - 2013</div>
  <div class="foot">KEEN MOTION</div><div class="mark"></div>
</section>

<section class="slide">
  <div class="pnum"></div>
  <div class="title">Our Values</div>
  <div class="ico" style="left:34px;top:48px;width:12px;height:12px"></div><div class="ico" style="left:74px;top:48px;width:12px;height:12px"></div><div class="ico" style="left:114px;top:48px;width:12px;height:12px"></div><div class="ico" style="left:154px;top:48px;width:12px;height:12px"></div>
  <div class="abs label" style="left:34px;top:64px">Home</div><div class="abs label" style="left:72px;top:64px">Support</div><div class="abs label" style="left:112px;top:64px">Chat 24/7</div><div class="abs label" style="left:152px;top:64px">Sending</div>
  <p class="abs copy" style="left:26px;top:70px;width:30px">A short line on this value.</p><p class="abs copy" style="left:66px;top:70px;width:30px">A short line on this value.</p><p class="abs copy" style="left:106px;top:70px;width:30px">A short line on this value.</p><p class="abs copy" style="left:146px;top:70px;width:30px">A short line on this value.</p>
  <div class="foot">KEEN MOTION</div><div class="mark"></div>
</section>

<section class="slide">
  <div class="pnum"></div>
  <div class="abs" style="left:78px;top:14px;width:84px;height:76px;border:4px solid #f0f0f0"></div>
  <div class="abs" style="left:40px;top:24px;font-weight:300;font-size:7px;line-height:1.2;color:#666">We have the<br>best technology<br>of the world<br><span style="color:var(--ink)">for less money</span></div>
  <div class="btn" style="left:40px;top:62px;width:20px;height:4px">Best Sports</div>
  <div class="ph face" style="left:130px;top:66px;width:30px;height:34px;clip-path:polygon(50% 0,100% 25%,100% 75%,50% 100%,0 75%,0 25%)" role="img" aria-label="Portrait of the coach"></div>
  <div class="foot">KEEN MOTION</div><div class="mark"></div>
</section>

<section class="slide">
  <div class="pnum"></div>
  <div class="title">Our Process</div>
  <div class="ico" style="left:42px;top:46px;width:12px;height:12px;border:none"><svg viewBox="0 0 12 12" width="12" height="12"><path d="M1 6 6 1.5 11 6M2.5 5v6h7V5" fill="none" stroke="#1e1e1e" stroke-width="1"/></svg></div>
  <div class="ico" style="left:92px;top:46px;width:12px;height:12px"></div>
  <div class="ico" style="left:142px;top:46px;width:12px;height:12px"></div>
  <div class="abs" style="left:62px;top:52px;width:20px;height:.5px;background:#bbb"></div><div class="abs" style="left:112px;top:52px;width:20px;height:.5px;background:#bbb"></div>
  <div class="abs label" style="left:40px;top:62px">Step 1</div><div class="abs label" style="left:90px;top:62px">Step 2</div><div class="abs label" style="left:140px;top:62px">Step 3</div>
  <p class="abs copy" style="left:30px;top:68px;width:36px">Plan the season and set goals.</p><p class="abs copy" style="left:80px;top:68px;width:36px">Train with clear daily drills.</p><p class="abs copy" style="left:130px;top:68px;width:36px">Review results and adjust.</p>
  <div class="foot">KEEN MOTION</div><div class="mark"></div>
</section>

<!-- row 4 -->
<section class="slide">
  <div class="pnum"></div>
  <div class="title">Our Process</div>
  <div class="abs" style="left:0;right:0;top:58px;height:.8px;background:var(--ink)"></div>
  <div class="ico" style="left:22px;top:44px;width:8px;height:8px"></div><div class="ico" style="left:73px;top:62px;width:8px;height:8px"></div><div class="ico" style="left:118px;top:44px;width:8px;height:8px"></div><div class="ico" style="left:163px;top:62px;width:8px;height:8px"></div><div class="ico" style="left:210px;top:44px;width:8px;height:8px"></div>
  <div class="ico" style="left:166px;top:44px;width:8px;height:8px"></div><div class="ico" style="left:118px;top:62px;width:8px;height:8px"></div>
  <div class="abs label" style="left:22px;top:64px">Step 01</div><div class="abs label" style="left:50px;top:52px">Step 02</div><div class="abs label" style="left:96px;top:64px">Step 03</div><div class="abs label" style="left:140px;top:52px">Step 04</div><div class="abs label" style="left:164px;top:72px">Step 05</div>
  <div class="foot">KEEN MOTION</div><div class="mark"></div>
</section>

<section class="slide">
  <div class="pnum"></div>
  <div class="title">Our Services</div>
  <div class="abs label" style="left:24px;top:40px">Marketing</div><div class="bar" style="left:24px;top:47px;width:64px"><i style="width:100%"></i></div>
  <div class="abs label" style="left:24px;top:62px">Social Media</div><div class="bar" style="left:24px;top:69px;width:64px"><i style="width:90%;background:var(--blue)"></i></div>
  <div class="abs label" style="left:24px;top:84px">Inbound Market</div><div class="bar" style="left:24px;top:91px;width:64px"><i style="width:88%"></i></div>
  <div class="abs label" style="left:108px;top:40px">Sports Strategy</div><div class="bar" style="left:108px;top:47px;width:64px"><i style="width:46%;background:var(--accent)"></i></div>
  <div class="abs label" style="left:108px;top:62px">Management</div><div class="bar g" style="left:108px;top:69px;width:64px"><i style="width:94%"></i></div>
  <div class="abs label" style="left:108px;top:84px">Consulting</div><div class="bar g" style="left:108px;top:91px;width:64px"><i style="width:84%"></i></div>
  <div class="foot">KEEN MOTION</div><div class="mark"></div>
</section>

<section class="slide" style="background:linear-gradient(180deg,#111526,#1e2444)">
  <div class="ph" style="inset:0;background:linear-gradient(160deg,rgba(40,50,90,.6),rgba(10,10,20,.2))" role="img" aria-label="Athletes in a dark stadium"></div>
  <div class="pnum"></div>
  <div class="title sans light">Our Services</div>
  <div class="numrow" style="left:34px;top:38px;color:#fff">01</div><div class="numrow" style="left:83px;top:38px;color:#fff">02</div><div class="numrow" style="left:132px;top:38px;color:#fff">03</div>
  <div class="numrow" style="left:34px;top:72px;color:#fff">04</div><div class="numrow" style="left:83px;top:72px;color:#fff">05</div><div class="numrow" style="left:132px;top:72px;color:#fff">06</div>
  <p class="abs copy white" style="left:32px;top:52px;width:34px;text-align:center">Short service note.</p><p class="abs copy white" style="left:81px;top:52px;width:34px;text-align:center">Short service note.</p><p class="abs copy white" style="left:130px;top:52px;width:34px;text-align:center">Short service note.</p>
  <p class="abs copy white" style="left:32px;top:86px;width:34px;text-align:center">Short service note.</p><p class="abs copy white" style="left:81px;top:86px;width:34px;text-align:center">Short service note.</p><p class="abs copy white" style="left:130px;top:86px;width:34px;text-align:center">Short service note.</p>
</section>

<section class="slide">
  <div class="pnum"></div>
  <div class="title sans">Our Services</div>
  <div class="numrow" style="left:34px;top:38px">01</div><div class="numrow" style="left:83px;top:38px">02</div><div class="numrow" style="left:132px;top:38px">03</div>
  <div class="numrow" style="left:34px;top:72px">04</div><div class="numrow" style="left:83px;top:72px">05</div><div class="numrow" style="left:132px;top:72px">06</div>
  <p class="abs copy" style="left:32px;top:52px;width:34px;text-align:center">Short service note.</p><p class="abs copy" style="left:81px;top:52px;width:34px;text-align:center">Short service note.</p><p class="abs copy" style="left:130px;top:52px;width:34px;text-align:center">Short service note.</p>
  <p class="abs copy" style="left:32px;top:86px;width:34px;text-align:center">Short service note.</p><p class="abs copy" style="left:81px;top:86px;width:34px;text-align:center">Short service note.</p><p class="abs copy" style="left:130px;top:86px;width:34px;text-align:center">Short service note.</p>
  <div class="foot">KEEN MOTION</div><div class="mark"></div>
</section>

<section class="slide" style="background:linear-gradient(120deg,#e3581f 0%,#c9502e 50%,#6b2f4a 100%)">
  <div class="pnum"></div>
  <div class="title sans light">Our Services</div>
  <div class="numrow" style="left:10px;top:48px;color:#fff;font-size:6px;width:40px">3,567</div><div class="numrow" style="left:58px;top:48px;color:#fff;font-size:6px;width:40px">758</div><div class="numrow" style="left:104px;top:48px;color:#fff;font-size:6px;width:40px">8,263</div><div class="numrow" style="left:148px;top:48px;color:#fff;font-size:6px;width:40px">8,263</div>
  <div class="abs label" style="left:20px;top:58px;color:#fff">Happy Clients</div><div class="abs label" style="left:66px;top:58px;color:#fff">Cups of Coffee</div><div class="abs label" style="left:116px;top:58px;color:#fff">Retweets</div><div class="abs label" style="left:160px;top:58px;color:#fff">Retweets</div>
  <p class="abs copy white" style="left:14px;top:64px;width:168px">Add a short note under each number to explain it.</p>
</section>

<section class="slide">
  <div class="pnum"></div>
  <div class="title sans">Our Services</div>
  <div class="numrow" style="left:10px;top:48px;font-size:6px;width:40px">3,567</div><div class="numrow" style="left:58px;top:48px;font-size:6px;width:40px">758</div><div class="numrow" style="left:104px;top:48px;font-size:6px;width:40px">8,263</div><div class="numrow" style="left:148px;top:48px;font-size:6px;width:40px">8,263</div>
  <div class="abs label" style="left:20px;top:58px">Happy Clients</div><div class="abs label" style="left:66px;top:58px">Cups of Coffee</div><div class="abs label" style="left:116px;top:58px">Retweets</div><div class="abs label" style="left:160px;top:58px">Retweets</div>
  <p class="abs copy" style="left:14px;top:64px;width:168px">Add a short note under each number to explain it.</p>
  <div class="foot">KEEN MOTION</div><div class="mark"></div>
</section>

<!-- row 5 -->
<section class="slide" style="background:linear-gradient(135deg,#f49a2a 0%,#f0632e 50%,#e63a5a 100%)">
  <div class="title sans light">Our Services</div>
  <div class="ico" style="left:16px;top:38px;border-color:#fff"></div><div class="ico" style="left:72px;top:38px;border-color:#fff"></div><div class="ico" style="left:128px;top:38px;border-color:#fff"></div>
  <div class="ico" style="left:16px;top:72px;border-color:#fff"></div><div class="ico" style="left:72px;top:72px;border-color:#fff"></div><div class="ico" style="left:128px;top:72px;border-color:#fff"></div>
  <p class="abs copy white" style="left:28px;top:38px;width:40px">Fast sports. A short line about it.</p><p class="abs copy white" style="left:84px;top:38px;width:40px">Support. A short line about it.</p><p class="abs copy white" style="left:140px;top:38px;width:40px">Exclusive. A short line about it.</p>
  <p class="abs copy white" style="left:28px;top:72px;width:40px">Worldwide. A short line about it.</p><p class="abs copy white" style="left:84px;top:72px;width:40px">Our stars. A short line about it.</p><p class="abs copy white" style="left:140px;top:72px;width:40px">Online chat. A short line about it.</p>
</section>

<section class="slide">
  <div class="pnum"></div>
  <div class="title sans">Our Services</div>
  <div class="ico" style="left:16px;top:38px"></div><div class="ico" style="left:72px;top:38px"></div><div class="ico" style="left:128px;top:38px"></div>
  <div class="ico" style="left:16px;top:72px"></div><div class="ico" style="left:72px;top:72px"></div><div class="ico" style="left:128px;top:72px"></div>
  <p class="abs copy" style="left:28px;top:38px;width:40px">Fast sports. A short line about it.</p><p class="abs copy" style="left:84px;top:38px;width:40px">Support. A short line about it.</p><p class="abs copy" style="left:140px;top:38px;width:40px">Exclusive. A short line about it.</p>
  <p class="abs copy" style="left:28px;top:72px;width:40px">Worldwide. A short line about it.</p><p class="abs copy" style="left:84px;top:72px;width:40px">Our stars. A short line about it.</p><p class="abs copy" style="left:140px;top:72px;width:40px">Online chat. A short line about it.</p>
  <div class="foot">KEEN MOTION</div><div class="mark"></div>
</section>

<section class="slide">
  <div class="pnum"></div>
  <div class="title sans">Our Partners</div>
  <div class="abs" style="left:36px;top:36px;width:124px;height:44px;border-top:.5px solid #ddd"></div>
  <div class="abs" style="left:36px;top:58px;width:124px;height:.5px;background:#ddd"></div>
  <div class="abs label" style="left:44px;top:44px;letter-spacing:1px">Northfield</div><div class="abs label" style="left:90px;top:44px">Corner Grind</div><div class="abs" style="left:122px;top:44px;width:4px;height:4px;background:var(--ink)"></div><div class="abs label" style="left:146px;top:44px">Bluepeak</div>
  <div class="abs label" style="left:44px;top:66px">Corner Grind</div><div class="abs label" style="left:90px;top:66px">Bluepeak</div><div class="abs label" style="left:118px;top:66px;letter-spacing:1px">Northfield</div><div class="abs" style="left:150px;top:66px;width:4px;height:4px;background:var(--ink)"></div>
  <div class="foot">KEEN MOTION</div><div class="mark"></div>
</section>

<section class="slide">
  <div class="pnum"></div>
  <div class="title">Our Partners</div>
  <div class="ph track" style="left:20px;top:38px;width:36px;height:32px" role="img" aria-label="Track lane number"></div>
  <div class="ph shot" style="left:60px;top:38px;width:36px;height:32px" role="img" aria-label="Athlete in dark light"></div>
  <div class="ph track-r" style="left:100px;top:38px;width:36px;height:32px" role="img" aria-label="Red track lanes"></div>
  <div class="ph track" style="left:140px;top:38px;width:36px;height:32px" role="img" aria-label="Blue track lanes"></div>
  <p class="abs copy" style="left:30px;top:80px;width:136px;text-align:center">Thank the partners who support your program in one short line.</p>
  <div class="foot">KEEN MOTION</div><div class="mark"></div>
</section>

<section class="slide">
  <div class="pnum"></div>
  <div class="title">Meet Our Coach</div>
  <div class="abs" style="left:30px;top:40px;font-size:7px;font-weight:300;color:#aaa;font-style:normal">I'm <b style="font-weight:600;color:var(--ink)">Dorian</b></div>
  <div class="abs" style="left:30px;top:49px;font-size:7px;font-weight:300;color:#aaa">Senior <b style="font-weight:600;color:var(--ink)">COACH</b></div>
  <p class="abs copy" style="left:30px;top:62px;width:70px">A short line about your coaching story and the teams you help.</p>
  <div class="ph face" style="left:116px;top:30px;width:62px;height:64px" role="img" aria-label="Portrait of Coach Dorian"></div>
  <div class="foot">KEEN MOTION</div><div class="mark"></div>
</section>

<section class="slide">
  <div class="pnum"></div>
  <div class="title">Our Team</div>
  <div class="ph face" style="left:30px;top:38px;width:24px;height:26px" role="img" aria-label="Team member portrait"></div><div class="ph face" style="left:74px;top:38px;width:24px;height:26px" role="img" aria-label="Team member portrait"></div><div class="ph face" style="left:118px;top:38px;width:24px;height:26px" role="img" aria-label="Team member portrait"></div><div class="ph face" style="left:162px;top:38px;width:24px;height:26px" role="img" aria-label="Team member portrait"></div>
  <div class="abs label" style="left:30px;top:68px">Alex Marin</div><div class="abs label" style="left:74px;top:68px">Nora Vale</div><div class="abs label" style="left:116px;top:68px">Lena Brooks</div><div class="abs label" style="left:160px;top:68px">Owen Tate</div>
  <div class="foot">KEEN MOTION</div><div class="mark"></div>
</section>

<!-- row 6 -->
<section class="slide">
  <div class="pnum"></div>
  <div class="title">Our Team</div>
  <div class="ph face" style="left:28px;top:34px;width:40px;height:40px" role="img" aria-label="Team member portrait"></div>
  <div class="ph face" style="left:78px;top:34px;width:40px;height:40px" role="img" aria-label="Team member portrait"></div>
  <div class="ph face" style="left:128px;top:34px;width:40px;height:40px" role="img" aria-label="Team member portrait"></div>
  <div class="abs" style="left:78px;top:74px;width:40px;height:1.2px;background:var(--accent)"></div>
  <div class="abs label" style="left:36px;top:84px">Mark Ives</div><div class="abs label" style="left:86px;top:84px">Jamie Cole</div><div class="abs label" style="left:136px;top:84px">Ross Lane</div>
  <div class="foot">KEEN MOTION</div><div class="mark"></div>
</section>

<section class="slide">
  <div class="pnum"></div>
  <div class="title sans">Our Team</div>
  <div class="abs" style="left:22px;top:34px;width:34px;height:44px;background:#f0f0f0"></div><div class="abs" style="left:63px;top:34px;width:34px;height:44px;background:#f0f0f0"></div><div class="abs" style="left:104px;top:34px;width:34px;height:44px;background:#f0f0f0"></div><div class="abs" style="left:145px;top:34px;width:34px;height:44px;background:#f0f0f0"></div>
  <div class="abs label" style="left:26px;top:82px">Alex Marin</div><div class="abs label" style="left:68px;top:82px">Nora Vale</div><div class="abs label" style="left:107px;top:82px">Lena Brooks</div><div class="abs label" style="left:150px;top:82px">Owen Tate</div>
  <div class="foot">KEEN MOTION</div><div class="mark"></div>
</section>

<section class="slide" style="background:linear-gradient(120deg,#1c2248,#332a5a)">
  <div class="title light">Meet Our Team</div>
  <div class="abs" style="left:22px;top:38px;width:34px;height:44px;background:#fff"></div><div class="abs" style="left:63px;top:38px;width:34px;height:44px;background:#fff"></div><div class="abs" style="left:104px;top:38px;width:34px;height:44px;background:#fff"></div><div class="abs" style="left:145px;top:38px;width:34px;height:44px;background:#fff"></div>
  <div class="ph face" style="left:31px;top:42px;width:16px;height:16px;border-radius:50%" role="img" aria-label="Portrait"></div><div class="ph face" style="left:72px;top:42px;width:16px;height:16px;border-radius:50%" role="img" aria-label="Portrait"></div><div class="ph face" style="left:113px;top:42px;width:16px;height:16px;border-radius:50%" role="img" aria-label="Portrait"></div><div class="ph face" style="left:154px;top:42px;width:16px;height:16px;border-radius:50%" role="img" aria-label="Portrait"></div>
  <div class="abs label" style="left:26px;top:64px">Alex Marin</div><div class="abs label" style="left:68px;top:64px">Nora Vale</div><div class="abs label" style="left:107px;top:64px">Lena Brooks</div><div class="abs label" style="left:150px;top:64px">Owen Tate</div>
</section>

<section class="slide">
  <div class="pnum"></div>
  <div class="title">Our Projects</div>
  <div class="ph track-r" style="left:0;top:38px;width:110px;height:50px" role="img" aria-label="Red track lanes"></div>
  <div class="ph shot" style="left:110px;top:38px;width:30px;height:50px" role="img" aria-label="Athlete in dark light"></div>
  <div class="ph track" style="left:140px;top:38px;width:56px;height:50px" role="img" aria-label="Blue track lanes"></div>
  <div class="foot">KEEN MOTION</div><div class="mark"></div>
</section>

<section class="slide">
  <div class="pnum"></div>
  <div class="title">Our Projects</div>
  <div class="ph track" style="left:14px;top:48px;width:60px;height:52px" role="img" aria-label="Blue track lanes"></div>
  <div class="abs" style="left:120px;top:36px;font-size:5px;font-weight:600;line-height:1.2;text-align:center">Project<br>2017 Works</div>
  <p class="abs copy" style="left:100px;top:50px;width:78px">Explain the project, the team and the result in a few short lines.</p>
  <div class="btn" style="left:128px;top:68px;width:22px;height:4px">Creative Works</div>
  <div class="foot">KEEN MOTION</div><div class="mark"></div>
</section>

<section class="slide">
  <div class="pnum"></div>
  <div class="title">Our Projects</div>
  <div class="abs" style="left:66px;top:36px;font-size:5px;font-weight:600;line-height:1.2;text-align:center">Project<br>2017 Works</div>
  <p class="abs copy" style="left:40px;top:50px;width:78px">Explain the project, the team and the result in a few short lines.</p>
  <div class="btn" style="left:68px;top:68px;width:22px;height:4px">Creative Works</div>
  <div class="ph track" style="left:140px;top:48px;width:56px;height:52px" role="img" aria-label="Blue track lanes"></div>
  <div class="foot">KEEN MOTION</div><div class="mark"></div>
</section>

<!-- row 7 -->
<section class="slide">
  <div class="ph track" style="left:0;top:0;width:62px;height:56px" role="img" aria-label="Blue track lanes"></div>
  <div class="ph shot" style="left:62px;top:0;width:62px;height:56px" role="img" aria-label="Athlete in dark light"></div>
  <div class="ph track-r" style="left:0;top:56px;width:62px;height:54px" role="img" aria-label="Red track lanes"></div>
  <div class="ph track" style="left:62px;top:56px;width:62px;height:54px" role="img" aria-label="Track lane numbers"></div>
  <div class="abs big" style="left:132px;top:36px;font-size:7px;text-align:center;width:56px">Masonry<br>Left Layout</div>
  <p class="abs copy" style="left:132px;top:54px;width:56px">Describe this gallery in one short line of text.</p>
</section>

<section class="slide">
  <div class="abs big" style="left:8px;top:36px;font-size:7px;text-align:center;width:56px">Masonry<br>Right Layout</div>
  <p class="abs copy" style="left:8px;top:54px;width:56px">Describe this gallery in one short line of text.</p>
  <div class="ph shot" style="left:72px;top:0;width:62px;height:56px" role="img" aria-label="Athletes in dark light"></div>
  <div class="ph track-r" style="left:134px;top:0;width:62px;height:56px" role="img" aria-label="Red track lanes"></div>
  <div class="ph track" style="left:72px;top:56px;width:62px;height:54px" role="img" aria-label="Blue track lanes"></div>
  <div class="ph track" style="left:134px;top:56px;width:62px;height:54px" role="img" aria-label="Track lane numbers"></div>
</section>

<section class="slide">
  <div class="ph track" style="left:0;top:0;width:46px;height:42px" role="img" aria-label="Blue track lanes"></div>
  <div class="ph track" style="left:46px;top:0;width:84px;height:42px" role="img" aria-label="Track lane numbers"></div>
  <div class="ph shot" style="left:46px;top:42px;width:38px;height:68px" role="img" aria-label="Athlete in dark light"></div>
  <div class="ph track-r" style="left:84px;top:60px;width:46px;height:50px" role="img" aria-label="Red track lanes"></div>
  <div class="abs big" style="left:140px;top:36px;font-size:7px">Project<br>2017 Works</div>
  <p class="abs copy" style="left:140px;top:54px;width:50px">Share the story of this project in short lines.</p>
</section>

<section class="slide">
  <div class="pnum"></div>
  <div class="title sans">Our Projects</div>
  <div class="abs" style="left:0;top:30px;width:196px;height:80px;display:grid;grid-template-columns:repeat(6,1fr);grid-template-rows:1fr 1fr">
    <div style="background:#8f8f8f"></div><div class="track-r" role="img" aria-label="Red track"></div><div style="background:#8f8f8f"></div><div class="track-r" role="img" aria-label="Red track"></div><div class="track" role="img" aria-label="Blue track"></div><div style="background:#8f8f8f"></div>
    <div class="track" role="img" aria-label="Blue track"></div><div style="background:#8f8f8f"></div><div class="track-r" role="img" aria-label="Red track"></div><div style="background:#8f8f8f"></div><div class="track" role="img" aria-label="Blue track"></div><div class="track" role="img" aria-label="Blue track"></div>
  </div>
  <div class="abs label" style="left:8px;top:48px;color:#fff">Fast Sports</div><div class="abs label" style="left:74px;top:48px;color:#fff">Fast Sports</div><div class="abs label" style="left:172px;top:48px;color:#fff">Fast Sports</div>
  <div class="abs label" style="left:42px;top:86px;color:#fff">Fast Sports</div><div class="abs label" style="left:106px;top:86px;color:#fff">Fast Sports</div>
</section>

<section class="slide dark">
  <div class="ph shot" style="left:0;top:0;width:30px;height:110px" role="img" aria-label="Athlete in dark light"></div>
  <div class="ph track" style="left:30px;top:0;width:50px;height:56px" role="img" aria-label="Blue track lanes"></div>
  <div class="ph track" style="left:80px;top:0;width:50px;height:56px" role="img" aria-label="Track lane numbers"></div>
  <div class="ph track-r" style="left:30px;top:56px;width:50px;height:54px" role="img" aria-label="Red track lanes"></div>
  <div class="ph track" style="left:80px;top:56px;width:50px;height:54px" role="img" aria-label="Blue track lanes"></div>
  <div class="abs" style="left:130px;top:0;width:66px;height:110px;background:#fff"></div>
  <div class="abs big" style="left:136px;top:28px;font-size:6.5px">Creative Left<br>Masonry</div>
  <p class="abs copy" style="left:136px;top:46px;width:54px">Describe this set of images in a short line.</p>
  <div class="btn" style="left:144px;top:68px;width:24px;height:4px">Creative Works</div>
</section>

<section class="slide">
  <div class="abs big" style="left:8px;top:28px;font-size:6.5px">Creative<br>Masonry</div>
  <p class="abs copy" style="left:8px;top:46px;width:54px">Describe this set of images in a short line.</p>
  <div class="btn" style="left:14px;top:68px;width:24px;height:4px">Creative Works</div>
  <div class="ph track" style="left:70px;top:0;width:42px;height:56px" role="img" aria-label="Blue track lanes"></div>
  <div class="ph track" style="left:112px;top:0;width:84px;height:56px" role="img" aria-label="Track lane numbers"></div>
  <div class="ph track-r" style="left:70px;top:56px;width:84px;height:54px" role="img" aria-label="Red track lanes"></div>
  <div class="ph track" style="left:154px;top:56px;width:42px;height:54px" role="img" aria-label="Blue track lanes"></div>
</section>

<!-- row 8 -->
<section class="slide">
  <div class="abs big" style="left:32px;top:32px;font-size:7px;text-align:right;width:74px">Project<br>2017 Works</div>
  <p class="abs copy" style="left:24px;top:52px;width:90px">Tell the story of this project in two short lines for the room.</p>
  <div class="ph track" style="left:116px;top:0;width:80px;height:44px" role="img" aria-label="Track lane numbers"></div>
  <div class="ph shot" style="left:116px;top:44px;width:40px;height:66px" role="img" aria-label="Athlete in dark light"></div>
  <div class="ph track-r" style="left:156px;top:66px;width:40px;height:44px" role="img" aria-label="Red track lanes"></div>
</section>

<section class="slide">
  <div class="abs label" style="left:26px;top:16px;font-size:3px;letter-spacing:.5px">Great Times</div>
  <p class="abs copy" style="left:20px;top:22px;width:50px;text-align:center">Share moments of joy.</p>
  <div class="ph shot" style="left:98px;top:0;width:98px;height:110px" role="img" aria-label="Team celebrating in dark arena"></div>
  <div class="ph track-r" style="left:0;top:52px;width:98px;height:58px" role="img" aria-label="Red track lanes"></div>
  <div class="abs label" style="left:130px;top:78px;color:#fff;letter-spacing:.5px">Enjoy the Life</div>
</section>

<section class="slide">
  <div class="abs big" style="left:14px;top:30px;font-size:7px">About Us<br>Image Layout</div>
  <p class="abs copy" style="left:14px;top:50px;width:60px">Write a few short lines that explain who you are and what you do.</p>
  <div class="ph track" style="left:84px;top:0;width:112px;height:110px" role="img" aria-label="Blue track lanes with large numbers"></div>
  <div class="foot">KEEN MOTION</div>
</section>

<section class="slide">
  <div class="ph face" style="left:0;top:0;width:98px;height:110px" role="img" aria-label="Portrait of Coach Dorian"></div>
  <div class="abs big" style="left:108px;top:32px;font-size:7px">All<br>About<br>Coach Dorian</div>
  <p class="abs copy" style="left:108px;top:58px;width:78px">A short story about the coach and the road behind each season.</p>
  <div class="mark"></div>
</section>

<section class="slide">
  <div class="abs label" style="left:18px;top:26px;font-size:3px;letter-spacing:.5px">Best Sports</div>
  <div class="abs" style="left:18px;top:36px;font-size:10px;font-weight:300;line-height:1.15;color:#aaa">Sports<br>Life &amp;<br><span style="color:var(--ink)">Join</span></div>
  <div class="ph track" style="left:92px;top:0;width:104px;height:110px" role="img" aria-label="Track lane numbers"></div>
  <div class="abs" style="left:100px;top:66px;width:26px;height:30px;background:#111"></div>
  <div class="abs label" style="left:104px;top:72px;color:#fff">Sports<br>in the world</div>
</section>

<section class="slide" style="background:linear-gradient(180deg,#1a2145,#2c3470)">
  <div class="ph" style="inset:0;background:linear-gradient(160deg,rgba(80,100,170,.3),rgba(0,0,0,0))" role="img" aria-label="Track lanes at night"></div>
  <div class="abs" style="left:22px;top:8px;width:152px;height:92px;border:.6px solid rgba(255,255,255,.2)"></div>
  <div class="abs big" style="left:22px;top:44px;width:152px;text-align:center;color:#fff;font-size:6px;line-height:1.3">We travel not to escape life<br>but for life not to escape us</div>
  <div class="abs" style="left:10px;top:50px;color:#fff;font-size:6px">&larr;</div><div class="abs" style="left:180px;top:50px;color:#fff;font-size:6px">&rarr;</div>
</section>

<!-- row 9 -->
<section class="slide">
  <div class="pnum"></div>
  <div class="title">Clustered Chart</div>
  <svg class="abs" style="left:16px;top:34px" width="70" height="60" viewBox="0 0 70 60">
    <line x1="2" y1="58" x2="68" y2="58" stroke="#ccc" stroke-width=".5"/>
    <rect x="16" y="14" width="10" height="44" fill="#1e1e1e"/><rect x="28" y="34" width="10" height="24" fill="#2f6cc9"/><rect x="40" y="22" width="10" height="36" fill="#2f6cc9"/><rect x="52" y="26" width="10" height="32" fill="#ec5a24"/>
  </svg>
  <div class="ico fill" style="left:100px;top:44px;width:7px;height:7px"></div><div class="ico blue" style="left:140px;top:44px;width:7px;height:7px"></div>
  <div class="ico orange" style="left:100px;top:68px;width:7px;height:7px"></div><div class="ico fill" style="left:140px;top:68px;width:7px;height:7px;background:#555"></div>
  <div class="abs label" style="left:100px;top:54px">Feature</div><div class="abs label" style="left:140px;top:54px">Name</div><div class="abs label" style="left:100px;top:78px">Function</div><div class="abs label" style="left:140px;top:78px">Element</div>
  <div class="foot">KEEN MOTION</div><div class="mark"></div>
</section>

<section class="slide">
  <div class="pnum"></div>
  <div class="title sans">Lines Chart</div>
  <div class="ico fill" style="left:24px;top:40px;width:7px;height:7px"></div><div class="ico blue" style="left:64px;top:40px;width:7px;height:7px"></div>
  <div class="ico orange" style="left:24px;top:66px;width:7px;height:7px"></div><div class="ico fill" style="left:64px;top:66px;width:7px;height:7px;background:#555"></div>
  <div class="abs label" style="left:24px;top:50px">Feature</div><div class="abs label" style="left:64px;top:50px">Name</div><div class="abs label" style="left:24px;top:76px">Function</div><div class="abs label" style="left:64px;top:76px">Element</div>
  <svg class="abs" style="left:110px;top:44px" width="66" height="36" viewBox="0 0 66 36" fill="none" stroke-width=".6">
    <polyline points="0,30 14,10 30,24 46,6 66,20" stroke="#999"/><polyline points="0,20 16,26 32,12 48,28 66,8" stroke="#bbb"/><polyline points="0,12 18,18 34,30 50,16 66,30" stroke="#777"/>
  </svg>
  <div class="foot">KEEN MOTION</div><div class="mark"></div>
</section>

<section class="slide">
  <div class="pnum"></div>
  <div class="title">Pie Chart</div>
  <svg class="abs" style="left:30px;top:36px" width="40" height="40" viewBox="0 0 40 40">
    <circle cx="20" cy="20" r="16" fill="none" stroke="#e6e6e6" stroke-width="3"/>
    <circle cx="20" cy="20" r="16" fill="none" stroke="#2f6cc9" stroke-width="3" stroke-dasharray="62.3 100.5" transform="rotate(-90 20 20)"/>
    <circle cx="20" cy="20" r="16" fill="none" stroke="#ec5a24" stroke-width="3" stroke-dasharray="14 100.5" stroke-dashoffset="-62.3" transform="rotate(-90 20 20)"/>
    <text x="20" y="24" text-anchor="middle" font-family="Open Sans, sans-serif" font-size="10" fill="#1e1e1e">62%</text>
  </svg>
  <div class="ico fill" style="left:100px;top:40px;width:7px;height:7px"></div><div class="ico blue" style="left:140px;top:40px;width:7px;height:7px"></div>
  <div class="ico orange" style="left:100px;top:66px;width:7px;height:7px"></div><div class="ico fill" style="left:140px;top:66px;width:7px;height:7px;background:#555"></div>
  <div class="abs label" style="left:100px;top:50px">Feature</div><div class="abs label" style="left:140px;top:50px">Name</div><div class="abs label" style="left:100px;top:76px">Function</div><div class="abs label" style="left:140px;top:76px">Element</div>
  <div class="foot">KEEN MOTION</div><div class="mark"></div>
</section>

<section class="slide">
  <div class="pnum"></div>
  <div class="title">Mountain Chart</div>
  <div class="ico fill" style="left:18px;top:40px;width:7px;height:7px"></div><div class="abs label" style="left:28px;top:41px">Something</div>
  <p class="abs copy" style="left:28px;top:46px;width:60px">A short note that explains this part of the chart.</p>
  <div class="ico fill" style="left:18px;top:68px;width:7px;height:7px;background:#555"></div><div class="abs label" style="left:28px;top:69px">Something</div>
  <p class="abs copy" style="left:28px;top:74px;width:60px">A short note that explains this part of the chart.</p>
  <svg class="abs" style="left:106px;top:40px" width="76" height="44" viewBox="0 0 76 44">
    <polygon points="0,44 0,14 16,4 34,24 50,10 62,20 76,8 76,44" fill="#1e1e1e"/>
    <polygon points="0,44 0,30 22,36 40,18 58,34 76,14 76,44" fill="#2f6cc9"/>
  </svg>
  <div class="foot">KEEN MOTION</div><div class="mark"></div>
</section>

<section class="slide">
  <div class="pnum"></div>
  <div class="title sans">Canada Map</div>
  <div class="ph" style="left:20px;top:36px;width:70px;height:50px;background:linear-gradient(120deg,#d8d8d8 60%,#ec5a24 75%,#d8d8d8 85%);border-radius:6px" role="img" aria-label="Map of Canada with one province highlighted"></div>
  <p class="abs copy" style="left:104px;top:34px;width:76px">Point out the regions where your program is active this year.</p>
  <div class="abs label" style="left:104px;top:54px">Ontario</div><div class="bar" style="left:104px;top:59px;width:70px;height:1.5px"><i style="width:80%;background:var(--accent)"></i></div>
  <div class="abs label" style="left:104px;top:64px">Quebec</div><div class="bar" style="left:104px;top:69px;width:70px;height:1.5px"><i style="width:60%;background:var(--accent)"></i></div>
  <div class="abs label" style="left:104px;top:74px">Alberta</div><div class="bar" style="left:104px;top:79px;width:70px;height:1.5px"><i style="width:45%;background:var(--accent)"></i></div>
  <div class="foot">KEEN MOTION</div><div class="mark"></div>
</section>

<section class="slide">
  <div class="pnum"></div>
  <div class="title sans">United States</div>
  <div class="ph" style="left:20px;top:40px;width:70px;height:42px;background:linear-gradient(120deg,#8d8d8d 0%,#bdbdbd 55%,#2f6cc9 85%,#bdbdbd 92%);border-radius:4px" role="img" aria-label="Map of the United States with states highlighted"></div>
  <p class="abs copy" style="left:104px;top:34px;width:76px">Point out the states where your teams compete this season.</p>
  <div class="abs label" style="left:104px;top:54px">Blue Region</div><div class="bar" style="left:104px;top:59px;width:70px;height:1.5px"><i style="width:80%;background:var(--blue)"></i></div>
  <div class="abs label" style="left:104px;top:64px">Dark Region</div><div class="bar" style="left:104px;top:69px;width:70px;height:1.5px"><i style="width:60%;background:var(--blue)"></i></div>
  <div class="abs label" style="left:104px;top:74px">Grey Region</div><div class="bar" style="left:104px;top:79px;width:70px;height:1.5px"><i style="width:45%;background:var(--blue)"></i></div>
  <div class="foot">KEEN MOTION</div><div class="mark"></div>
</section>

<!-- row 10 -->
<section class="slide">
  <div class="pnum"></div>
  <div class="title">Worldwide Map</div>
  <div class="ph" style="left:30px;top:30px;width:140px;height:66px;background:linear-gradient(100deg,#555 0%,#bbb 22%,#e9662c 34%,#bbb 45%,#2f6cc9 62%,#3d7ad6 80%,#bbb 92%);border-radius:10px" role="img" aria-label="World map with highlighted regions"></div>
  <div class="foot">KEEN MOTION</div><div class="mark"></div>
</section>

<section class="slide" style="background:linear-gradient(180deg,#18203f,#25305e)">
  <div class="ph" style="inset:0;background:linear-gradient(160deg,rgba(70,90,160,.35),rgba(0,0,0,0))" role="img" aria-label="Track lanes at night"></div>
  <svg class="abs" style="left:78px;top:26px" width="40" height="58" viewBox="0 0 40 58" fill="none" stroke="#fff" stroke-width=".5"><line x1="2" y1="2" x2="38" y2="56"/><line x1="38" y1="2" x2="2" y2="56"/><circle cx="30" cy="14" r="4"/><circle cx="10" cy="44" r="4"/></svg>
  <div class="abs" style="left:0;right:0;top:51px;text-align:center;color:#fff;font-size:5px;font-weight:600;letter-spacing:.3px">CREATIVE &nbsp;&nbsp;&nbsp;&nbsp;&nbsp;&nbsp;&nbsp;&nbsp; LAYOUTS</div>
</section>

<section class="slide" style="background:linear-gradient(90deg,#2fd6b4 0%,#4a86a8 50%,#5a3f8e 100%)">
  <div class="abs" style="left:62px;top:40px;width:72px;height:.5px;background:rgba(255,255,255,.6)"></div>
  <div class="abs" style="left:0;right:0;top:46px;text-align:center;color:#fff;font-size:11px;font-weight:600">Good Bye!</div>
  <div class="abs" style="left:0;right:0;top:61px;text-align:center;color:#fff;font-size:2.4px">Thanks for coming</div>
  <div class="abs" style="left:62px;top:68px;width:72px;height:.5px;background:rgba(255,255,255,.6)"></div>
</section>

<section class="slide" style="background:linear-gradient(180deg,#18203f,#25305e)">
  <div class="ph" style="inset:0;background:linear-gradient(160deg,rgba(70,90,160,.35),rgba(0,0,0,0))" role="img" aria-label="Track lanes at night"></div>
  <div class="abs" style="left:44px;top:22px;width:108px;height:26px;border:1px solid #fff;color:#fff;text-align:center;line-height:24px;font-size:11px;font-weight:600">CONTACT US</div>
  <svg class="abs" style="left:50px;top:64px" width="100" height="10" viewBox="0 0 100 10" fill="none" stroke="#fff" stroke-width=".6">
    <circle cx="8" cy="5" r="4.5"/><path d="M8 3a1.3 1.3 0 1 1 0 2.6A1.3 1.3 0 1 1 8 3M8 5.6v2"/>
    <circle cx="50" cy="5" r="4.5"/><rect x="47.5" y="3.5" width="5" height="3.5"/><path d="M47.5 3.5 50 5.5 52.5 3.5"/>
    <circle cx="92" cy="5" r="4.5"/><path d="M90.5 3c0 2.5 1.5 4 3 4l.6-.8-1-.7-.5.4c-.6-.3-1-.8-1.2-1.3l.4-.5-.6-1z"/>
  </svg>
  <div class="abs label" style="left:52px;top:78px;color:#fff">Address</div><div class="abs label" style="left:96px;top:78px;color:#fff">Email</div><div class="abs label" style="left:134px;top:78px;color:#fff">Telephone</div>
  <div class="abs copy white" style="left:44px;top:83px;width:28px;text-align:center">12 Rideau Lane, Ottawa</div>
  <div class="abs copy white" style="left:86px;top:83px;width:28px;text-align:center">hello@keenmotion.ca</div>
  <div class="abs copy white" style="left:128px;top:83px;width:28px;text-align:center">+1 613 555 0142</div>
</section>

</main>
</body>
</html>
```